Web Design For Metal Recycling Company

We are a scrap and recycling company dealing mainly in scrap metal base in Singapore. We deal in both domestic market and international market. Currently we are still unsure if we want to have a "lively" or "professional" company image so we will leave it to the designer to deem what is good.

We wish for a website to be able to "Retain" the interest of new visitor and at the same time able to give enough information for new and existing customer. We would also wish for design that will get the visitor to "Engage" us.

The attached is the logo for the company and we would want to incorporate that into the website. Either of the logo is fine.

```html
<!DOCTYPE html>
<html lang="en">
<head>
<meta charset="utf-8">
<title>Kai Tong Metals</title>
<link href="https://fonts.googleapis.com/css2?family=Lato:wght@400;700&display=swap" rel="stylesheet">
<style>
:root{
  --black:#000;
  --gold:#c9982a;
  --gold-light:#f3e3b8;
  --gold-footer:#d3a441;
  --text:#333;
  --grey-dark:#3b3b3b;
  --grey-border:#d6d6d6;
  --white:#fff;
}
*{box-sizing:border-box;margin:0;padding:0}
html,body{width:881px;height:1200px;overflow:hidden;background:var(--white)}
body{position:relative;font-family:'Lato',sans-serif;color:var(--text)}
.abs{position:absolute}
.site-header{left:0;top:0;width:881px;height:88px;background:var(--black)}
.brand{left:103px;top:8px;width:150px;text-align:center}
.brand-mark{display:block;margin:0 auto 6px;width:40px;height:40px;border:2px solid var(--gold)}
.brand-name{color:var(--gold);font-weight:700;font-size:14px;letter-spacing:1px;white-space:nowrap}
.phone{right:105px;top:18px;color:var(--white);font-size:15px;display:flex;align-items:center;gap:4px}
.nav{left:290px;top:57px;height:31px;display:flex;background:#2b2b2b}
.nav a{display:block;line-height:31px;font-size:10.4px;color:var(--white);text-decoration:none;border-right:1px solid #555;text-align:center;white-space:nowrap}
.nav a.active{background:var(--gold-light);color:#000;font-weight:700}
.hero{left:0;top:88px;width:881px;height:323px;border-top:3px solid var(--gold);border-bottom:3px solid var(--gold);
  background:linear-gradient(180deg,#a9c6dd 0%,#8fa9b8 35%,#5b5248 70%,#7a6653 100%)}
.feature{top:360px;width:110px;text-align:center}
.feature-box{width:110px;height:110px;border:4px solid var(--gold);background:linear-gradient(135deg,#fbf3de,#ead6a3);box-shadow:0 0 0 2px #eee;display:flex;align-items:center;justify-content:center}
.feature-label{margin-top:9px;font-size:12px;font-weight:700;color:#333;white-space:nowrap;margin-left:-20px;margin-right:-20px}
.intro{left:110px;top:515px;width:661px;text-align:center;font-size:11.5px;line-height:17.6px}
.read-more{left:0;top:580px;width:881px;text-align:center;color:var(--gold);font-size:11.5px}
.divider{left:120px;width:641px;height:1px;background:linear-gradient(90deg,transparent,#ddd,transparent)}
.section-title{left:0;top:638px;width:881px;text-align:center;font-size:17px;font-weight:700;color:#222}
.section-title span{color:var(--gold)}
.title-accent{left:340px;top:664px}
.product{top:693px;width:90px;height:90px;border:2px solid var(--gold);text-align:center}
.product svg{margin-top:10px}
.product-label{font-size:10.5px;color:#222;margin-top:4px}
.panel{top:844px;width:202px;height:168px;border:1px solid var(--grey-border)}
.panel-head{height:28px;background:linear-gradient(#555,#333);color:var(--white);font-size:16px;font-weight:700;padding:3px 9px}
.news{display:flex;gap:4px;margin:11px 8px 0}
.news-thumb{width:46px;height:40px;background:linear-gradient(#5f6f82,#2f3136);flex:none}
.news-text{font-size:9.5px;line-height:12px;font-weight:400}
.news-text b{display:flex;justify-content:space-between;font-weight:700}
.panel-link{position:absolute;right:12px;bottom:8px;font-size:9.5px;font-weight:700;text-decoration:underline}
.commit{padding:9px 10px;font-size:9.5px;line-height:14px;color:#555}
.map{margin:11px 10px;height:116px;background:linear-gradient(180deg,#dcdcdc,#cfd0cf);border:1px solid #bbb}
.site-footer{left:0;top:1037px;width:881px;height:163px;background:linear-gradient(#d19f35,#e2bd5b);color:var(--white)}
.foot-col{top:12px}
.foot-head{font-size:13px;font-weight:700;margin-bottom:8px}
.quick-links a{display:block;color:var(--white);text-decoration:none;font-size:9.5px;line-height:24px}
.field{width:154px;height:17px;background:var(--white);border:1px solid #ccc;margin-bottom:5px;color:#777;font-size:8.5px;padding:2px 4px}
.submit{display:inline-block;background:#333;color:var(--white);font-size:9.5px;font-weight:700;padding:2px 9px;border-radius:3px}
.info-row{display:flex;gap:8px;font-size:9.5px;line-height:13px;margin-bottom:13px}
.vline{top:20px;width:1px;height:130px;background:rgba(255,255,255,.35)}
.foot-brand{left:615px;top:18px;width:160px;text-align:center}
.foot-mark{display:block;margin:0 auto 10px;width:40px;height:40px;border:2px solid var(--white)}
.foot-name{font-weight:700;font-size:14px;letter-spacing:1px}
.socials{display:flex;gap:8px;justify-content:center;margin:10px 0 10px}
.socials span{width:22px;height:22px;border-radius:50%;background:var(--white)}
.copy{font-size:8.5px}
</style>
</head>
<body>
<header class="site-header abs">
  <div class="brand abs"><span class="brand-mark"></span><span class="brand-name">KAI TONG METALS</span></div>
  <div class="phone abs"><svg width="12" height="14" viewBox="0 0 12 14"><path d="M2 1l3 0 1 3-2 1c1 2 2 3 4 4l1-2 3 1 0 3c-6 1-11-4-10-10z" fill="#fff"/></svg>61234500</div>
  <nav class="nav abs">
    <a class="active" style="width:51px">Home</a><a style="width:59px">About Us</a><a style="width:109px">Products &amp; Services</a><a style="width:150px">Environmental Commitment</a><a style="width:55px">Location</a><a style="width:64px;border:0">Contact Us</a>
  </nav>
</header>

<div class="hero abs" role="img" aria-label="Photo of a truck tipping a blue skip container in a scrap metal yard"></div>

<div class="feature abs" style="left:154px"><div class="feature-box"><svg width="70" height="50" viewBox="0 0 70 50"><circle cx="18" cy="8" r="6" fill="#222"/><circle cx="52" cy="8" r="6" fill="#222"/><path d="M8 48V22q0-6 10-6t12 10l5 4-3 3-6-4v23z M62 48V22q0-6-10-6t-12 10l-5 4 3 3 6-4v23z" fill="#222"/></svg></div><div class="feature-label">BUYERS</div></div>
<div class="feature abs" style="left:306px"><div class="feature-box"><svg width="70" height="50" viewBox="0 0 70 50"><path d="M2 6h8l8 26h38l10-28" stroke="#222" stroke-width="4" fill="none"/><g fill="#222"><circle cx="20" cy="12" r="3"/><circle cx="28" cy="12" r="3"/><circle cx="36" cy="12" r="3"/><circle cx="44" cy="12" r="3"/><circle cx="52" cy="12" r="3"/><circle cx="24" cy="20" r="3"/><circle cx="32" cy="20" r="3"/><circle cx="40" cy="20" r="3"/><circle cx="48" cy="20" r="3"/><circle cx="24" cy="42" r="5"/><circle cx="48" cy="42" r="5"/></g></svg></div><div class="feature-label">SELLING</div></div>
<div class="feature abs" style="left:458px"><div class="feature-box"><svg width="70" height="70" viewBox="0 0 70 70"><g fill="#222"><rect x="18" y="4" width="12" height="12" rx="2"/><rect x="40" y="4" width="12" height="12" rx="2"/><rect x="8" y="26" width="12" height="12" rx="2" fill="#888"/><rect x="30" y="26" width="12" height="12" rx="2" fill="#aaa"/><rect x="52" y="26" width="12" height="12" rx="2" fill="#888"/><rect x="18" y="48" width="12" height="12" rx="2"/><rect x="40" y="48" width="12" height="12" rx="2"/></g></svg></div><div class="feature-label">SCRAP MANAGEMENT</div></div>
<div class="feature abs" style="left:610px"><div class="feature-box"><svg width="70" height="70" viewBox="0 0 70 70"><g fill="none" stroke="#222" stroke-width="9"><path d="M22 30l10-16 10 16"/><path d="M50 38l-8 16h-18"/><path d="M18 50l-6-10 6-10"/></g></svg></div><div class="feature-label">RECYCLE</div></div>

<p class="intro abs">With over 30 years of experience and strong foundation, the company constantly grows and expands to meet the ever growing demand of the recyclable scrap industry. The company vision is to provide high product quality and satisfying customer service to all our customers and suppliers from various countries .</p>
<div class="read-more abs">Read More ››</div>
<div class="divider abs" style="top:614px"></div>

<h2 class="section-title abs">Our <span>Products &amp; Services</span></h2>
<svg class="title-accent abs" width="200" height="14" viewBox="0 0 200 14"><path d="M0 0Q100 6 100 14Q100 6 200 0z" fill="#e6c36b"/></svg>

<div class="product abs" style="left:103px"><svg width="46" height="46" viewBox="0 0 46 46"><circle cx="23" cy="23" r="17" fill="none" stroke="#666" stroke-width="2" stroke-dasharray="20 6"/></svg><div class="product-label">PROCESS</div></div>
<div class="product abs" style="left:220px"><svg width="56" height="46" viewBox="0 0 56 46"><path d="M4 34l10-14h30l8 14z" fill="#999"/><path d="M14 20l8-10h18l4 10z" fill="#bbb"/></svg><div class="product-label">FERROUS</div></div>
<div class="product abs" style="left:337px"><svg width="56" height="46" viewBox="0 0 56 46"><path d="M4 8l44 20-6 10L2 16z" fill="#777"/><ellipse cx="6" cy="12" rx="5" ry="6" fill="#ccc"/></svg><div class="product-label">NON-FERROUS</div></div>
<div class="product abs" style="left:454px"><svg width="46" height="46" viewBox="0 0 46 46"><rect x="10" y="10" width="26" height="26" fill="none" stroke="#666" stroke-width="2"/><rect x="17" y="17" width="12" height="12" fill="none" stroke="#666" stroke-width="2"/><path d="M14 4v6M20 4v6M26 4v6M32 4v6M14 36v6M20 36v6M26 36v6M32 36v6M4 14h6M4 20h6M4 26h6M4 32h6M36 14h6M36 20h6M36 26h6M36 32h6" stroke="#666" stroke-width="2"/></svg><div class="product-label">ELECTRONICS</div></div>
<div class="product abs" style="left:571px"><svg width="46" height="46" viewBox="0 0 46 46"><circle cx="18" cy="28" r="9" fill="none" stroke="#777" stroke-width="6" stroke-dasharray="4 3"/><circle cx="32" cy="14" r="6" fill="none" stroke="#777" stroke-width="4" stroke-dasharray="3 2"/></svg><div class="product-label">MACHINERY</div></div>
<div class="product abs" style="left:688px"><svg width="56" height="46" viewBox="0 0 56 46"><rect x="6" y="22" width="20" height="14" fill="#777"/><circle cx="38" cy="26" r="12" fill="none" stroke="#888" stroke-width="5" stroke-dasharray="4 3"/></svg><div class="product-label">OTHERS</div></div>

<div class="divider abs" style="top:814px"></div>

<section class="panel abs" style="left:103px">
  <div class="panel-head">News &amp; Events</div>
  <div class="news"><div class="news-thumb" role="img" aria-label="News thumbnail photo"></div><div class="news-text"><b><u>Lorem ipsum</u><span>30 April, 2013</span></b>Lorem ipsum dolor sit amet, The consectetuer adipiscing elit, sed</div></div>
  <div class="news" style="margin-top:14px"><div class="news-thumb" role="img" aria-label="News thumbnail photo"></div><div class="news-text"><b><u>Lorem ipsum</u><span>30 April, 2013</span></b>Lorem ipsum dolor sit amet, The consectetuer adipiscing elit, sed</div></div>
  <span class="panel-link">View All</span>
</section>
<section class="panel abs" style="left:337px">
  <div class="panel-head">Our Commitment</div>
  <p class="commit">Lorem ipsum dolor sit amet, The Lorem is consectetuer adipiscing elit, sed Lorem ipsum dolor sit amet, The Lorem is Lorem consectetuer adipiscing elit, sed Lorem ipsum dolor sit amet, The Lorem is Lorem consectetuer adipiscing elit, sed Lorem ipsum dolor sit amet, The Lorem is Lorem consectetuer ...</p>
  <span class="panel-link">Read More</span>
</section>
<section class="panel abs" style="left:572px">
  <div class="panel-head">Location</div>
  <div class="map" role="img" aria-label="Street map showing the company location"></div>
</section>

<footer class="site-footer abs">
  <div class="foot-col abs quick-links" style="left:105px"><div class="foot-head">Quick Links</div><a>&gt; Home</a><a>&gt; About Us</a><a>&gt; Our Products</a><a>&gt; Our Services</a><a>&gt; Contact Us</a></div>
  <div class="vline abs" style="left:204px"></div>
  <div class="foot-col abs" style="left:229px"><div class="foot-head">Quick Contact</div><div class="field">Name</div><div class="field">Email Address</div><div class="field" style="height:40px">Comments</div><span class="submit">SUBMIT</span></div>
  <div class="vline abs" style="left:405px"></div>
  <div class="foot-col abs" style="left:428px"><div class="foot-head">Contact Info</div>
    <div class="info-row"><svg width="12" height="14" viewBox="0 0 12 14"><path d="M6 14C2 8 1 6 1 5a5 5 0 0110 0c0 1-1 3-5 9z" fill="#fff"/><circle cx="6" cy="5" r="2" fill="#d3a441"/></svg><span>Duis autem vel eum iriure<br>dolor in hendrerit in</span></div>
    <div class="info-row"><svg width="12" height="12" viewBox="0 0 12 14"><path d="M2 1l3 0 1 3-2 1c1 2 2 3 4 4l1-2 3 1 0 3c-6 1-11-4-10-10z" fill="#fff"/></svg><span>0123 456 789</span></div>
    <div class="info-row"><svg width="13" height="10" viewBox="0 0 13 10"><rect width="13" height="10" fill="#fff"/><path d="M0 0l6.5 5L13 0" stroke="#d3a441" fill="none"/></svg><span>info@kaitongmetals.com</span></div>
    <div class="info-row"><svg width="13" height="12" viewBox="0 0 13 12"><rect x="0" y="4" width="13" height="6" fill="#fff"/><rect x="3" y="0" width="7" height="4" fill="#fff"/></svg><span>0123 456 789</span></div>
  </div>
  <div class="vline abs" style="left:594px"></div>
  <div class="foot-brand abs"><span class="foot-mark"></span><span class="foot-name">KAI TONG METALS</span>
    <div class="socials"><span></span><span></span><span></span></div>
    <div class="copy">© 2014 Kaitongmetals. All right reserved.</div></div>
</footer>
</body>
</html>
```